Album Cover Art for New Single

Independent singer-songwriter and pianist, seeking design work for a new single "Walk Along the Harbor". Christian & Gospel music format. See attached for master recording.

This single is personal for me, so I'm looking for an image that really captures the heart of the message. Redemption, forgiveness, prodigals returning home to a loving father.
Updates

Target Market(s)

Millenials

Colors

Designer to choose colors to be used in the design.

Requirements
Must have
• simple graphic, must include the following text:
• Walk Along the Harbor
• Dale Fennimore
Should not have
• Avoid "cheesy" look and feel.

```html
<!DOCTYPE html>
<html lang="en">
<head>
<meta charset="utf-8">
<title>Walk Along the Harbor — Dale Fennimore</title>
<link rel="stylesheet" href="https://fonts.googleapis.com/css2?family=Montserrat:wght@300;400&display=swap">
<style>
  :root {
    --paper: #ffffff;
    --ink: #1e1e1e;
    --sky: #e6e6e6;
    --sky-low: #d2d2d2;
    --trees: #333333;
    --water: #8c8c8c;
    --water-deep: #6c6c6c;
    --streak: rgba(150, 150, 150, 0.55);
    --name: #f2f2f2;
  }
  html, body {
    margin: 0;
    padding: 0;
    width: 1198px;
    height: 1200px;
    overflow: hidden;
    background: var(--paper);
  }
  .cover {
    position: relative;
    width: 1198px;
    height: 1200px;
    background: var(--paper);
    font-family: "Montserrat", sans-serif;
  }
  .cover-photo {
    position: absolute;
    left: 65px;
    top: 65px;
    width: 1069px;
    height: 1064px;
    background: linear-gradient(180deg,
      var(--sky) 0%,
      var(--sky-low) 46%,
      #9a9a9a 52%,
      var(--trees) 57%,
      var(--trees) 64%,
      #5a5a5a 69%,
      var(--water) 76%,
      var(--water-deep) 100%);
  }
  .title {
    position: absolute;
    right: 48px;
    top: 168px;
    margin: 0;
    display: flex;
    flex-direction: column;
    align-items: flex-end;
    gap: 52px;
  }
  .title-line {
    position: relative;
    display: block;
    padding: 0 68px 0 0;
    font-weight: 300;
    font-size: 50px;
    line-height: 62px;
    letter-spacing: 0.38em;
    color: var(--ink);
    text-transform: uppercase;
  }
  .title-line::before {
    content: "";
    position: absolute;
    right: 0;
    top: 50%;
    width: calc(100% + 90px);
    height: 20px;
    transform: translateY(-50%);
    background: linear-gradient(90deg,
      transparent 0%,
      var(--streak) 12%,
      rgba(200,200,200,0.35) 35%,
      rgba(200,200,200,0.35) 75%,
      var(--streak) 88%,
      transparent 100%);
    filter: blur(3px);
    z-index: 0;
  }
  .title-line span {
    position: relative;
    z-index: 1;
  }
  .artist {
    position: absolute;
    right: 78px;
    top: 660px;
    margin: 0;
    font-weight: 400;
    font-size: 32px;
    letter-spacing: 0.26em;
    color: var(--name);
    text-transform: uppercase;
  }
</style>
</head>
<body>
  <main class="cover">
    <div class="cover-photo" role="img" aria-label="Black and white photograph of a young man in a flat cap and jacket, looking sideways, standing before a lake with a line of trees under a pale sky"></div>

    <h1 class="title">
      <span class="title-line"><span>Walk</span></span>
      <span class="title-line"><span>Along</span></span>
      <span class="title-line"><span>The</span></span>
      <span class="title-line"><span>Harbor</span></span>
    </h1>

    <p class="artist">Dale Fennimore</p>
  </main>
</body>
</html>
```